Thornbury Lettings Managment Ltd website

Need a website To inform people/clients of the services we provide. 5 pages total with a local feel. Bristol, UK. I have logo artwork already is like the look based on
incorporate the artwork attached for theme, feel and colours fonts info etc

To best describe the business have a brief look at www.fernwickhomes.example.co.uk which is a local firm offering the same services. This is for your ref only and not to be copied.

Target Market(s)

Property Investors/Landlords

Coding

Coded - Design and coding required

Number of Pages Required

5+ page

Colors
0392cd
f68d4d

Requirements
Must have
• local feel. Possibly using some local architecture or historic landmarks etc. This is fexible.
• most also be mobile device compatible
Nice to have
• the membership logos - files attached: KTB, DWF, GMV and safehold-example.co.uk

```html
<!DOCTYPE html>
<html lang="en">
<head>
<meta charset="utf-8">
<title>Thornbury Lettings Managment Ltd</title>
<link href="https://fonts.googleapis.com/css2?family=Montserrat:ital,wght@0,400;0,500;0,600;0,700;1,400&display=swap" rel="stylesheet">
<style>
:root{
  --navy:#1d5b7c;
  --blue:#1f7fb6;
  --topbar:#2d5d7a;
  --orange:#ef8d22;
  --text:#555b60;
  --muted:#9a9ea2;
  --rule:#3a7fa0;
  --panel:#f3f1f1;
  --track:#f1f1f1;
  --btn:#3c3c3c;
  --footer-dark:#2b2b2b;
  --band:#e4e4e6;
}
*{box-sizing:border-box;margin:0;padding:0}
html,body{width:1200px;height:3072px;overflow:hidden;background:#fff}
body{position:relative;font-family:"Montserrat",sans-serif;color:var(--text)}
.abs{position:absolute}

/* top bar */
.topbar{left:0;top:0;width:1200px;height:41px;background:var(--topbar);color:#fff;font-size:11px;font-weight:600;padding:12px 0 0 117px;white-space:nowrap}

/* header */
.header{left:0;top:41px;width:1200px;height:123px;background:#fff}
.brand{left:164px;top:30px;display:flex;align-items:center;gap:12px}
.brand-mark{width:40px;height:40px;background:var(--navy)}
.brand-name{font-size:30px;font-weight:700;color:var(--navy);line-height:1}
.brand-sub{font-size:13px;font-weight:700;color:var(--navy);margin-top:4px;line-height:1}
.nav{top:33px;font-size:15px;font-weight:500;color:var(--navy);letter-spacing:.5px}
.nav.active{color:var(--orange)}

/* hero */
.hero{left:0;top:164px;width:1200px;height:424px;background:linear-gradient(120deg,#d9b792 0%,#c99a74 35%,#b9785a 60%,#d3b190 100%)}
.hero-label{background:rgba(110,110,110,.78);color:#fff;text-transform:uppercase;white-space:nowrap}
.hero-welcome{left:774px;top:377px;width:289px;height:59px;font-size:50px;line-height:59px;text-align:center;font-weight:400}
.hero-line{right:131px;height:30px;font-size:18px;line-height:30px;padding:0 8px;font-weight:400}

/* back to top */
.to-top{left:1126px;width:45px;height:32px;background:var(--btn);display:flex;align-items:center;justify-content:center}

/* services */
.service-photo{top:662px;width:301px;height:200px;box-shadow:0 6px 8px rgba(0,0,0,.18)}
.service-title{top:884px;font-size:17px;font-weight:700;color:var(--orange);letter-spacing:.5px}
.service-copy{top:928px;width:300px;font-size:12.5px;line-height:19.5px;color:var(--text)}
.service-link{font-size:12.5px;color:#333;display:block;margin-top:22px}

/* dividers */
.divider-line{left:109px;width:983px;height:2px;background:var(--navy)}
.divider-diamond{width:36px;height:36px;background:var(--navy);transform:rotate(45deg)}

/* reliability */
.section-title{font-size:25px;font-weight:600;color:var(--navy);letter-spacing:.8px;line-height:45px;text-transform:uppercase;white-space:nowrap}
.stat{left:109px;width:368px;height:32px;background:var(--track)}
.stat-fill{height:32px;background:var(--blue);color:#fff;font-size:11.5px;font-weight:700;line-height:32px;padding-left:14px;white-space:nowrap}
.stat-fill.striped{background:repeating-linear-gradient(135deg,var(--blue) 0 14px,#3f95c6 14px 28px)}
.stat-label{position:absolute;left:14px;top:0;color:#fff;font-size:11.5px;font-weight:700;line-height:32px;white-space:nowrap}
.bridge-photo{left:518px;top:1475px;width:574px;height:378px;background:linear-gradient(180deg,#c9cfd6 0%,#b8c3c9 30%,#7f9472 55%,#496a34 80%,#3d5a2c 100%);box-shadow:0 6px 8px rgba(0,0,0,.2)}

/* testimonial */
.quote{left:618px;top:2030px;width:474px;height:137px;background:var(--panel);padding:18px 24px;font-size:12.5px;line-height:19px;font-style:italic;color:#7b8085}
.quote-tail{left:648px;top:2167px;width:0;height:0;border-left:10px solid transparent;border-right:10px solid transparent;border-top:12px solid var(--panel)}
.author{left:622px;top:2186px;display:flex;align-items:center;gap:16px;font-size:12px;color:#333}
.author b{font-weight:700}
.thin-rule{left:209px;top:2255px;width:784px;height:1px;background:var(--rule)}

/* connections */
.arrow-btn{top:2348px;width:26px;height:26px;background:#999;display:flex;align-items:center;justify-content:center}
.badge{background:#e7e9ec;border:1px solid #d4d7db}

/* footer */
.footer-band{left:0;top:2503px;width:1200px;height:16px;background:var(--band)}
.footer-brand{left:119px;top:2592px;display:flex;align-items:center;gap:8px}
.footer-brand .brand-mark{width:26px;height:26px}
.footer-brand .name{font-size:17px;font-weight:700;color:var(--navy);line-height:1}
.footer-brand .sub{font-size:8px;font-weight:700;color:var(--navy)}
.footer-about{left:109px;top:2675px;width:225px;font-size:11.5px;line-height:20px;color:var(--text)}
.footer-heading{top:2560px;font-size:12px;font-weight:700;color:var(--navy);letter-spacing:.5px}
.footer-menu{left:362px;top:2598px;width:226px;list-style:none}
.footer-menu li{height:43px;border-bottom:1px solid #bfc3c6;font-size:11px;color:var(--muted);line-height:22px}
.footer-menu li.current{color:var(--navy);font-weight:600}
.contact{left:614px;top:2600px;width:240px;font-size:11px;line-height:19px;color:var(--text);white-space:nowrap}
.contact span{color:var(--muted);font-size:10.3px}
.field-label{left:866px;font-size:11.5px;color:#333}
.field{left:866px;width:226px;border:1px solid #cfd2d4;background:#fff}
.send{left:866px;top:2931px;width:42px;height:20px;background:var(--orange);color:#fff;font-size:11px;font-weight:700;text-align:center;line-height:20px}
.bottombar{left:0;top:3010px;width:1200px;height:62px;background:var(--footer-dark);font-size:10.5px;color:#aaa;padding:23px 0 0 109px}
.social{top:3034px;width:14px;height:14px;border-radius:50%;background:#5a5a5a}
</style>
</head>
<body>

<div class="abs topbar">Call Us Today! 0117 496 0238 &nbsp;|&nbsp; hello@thornburylettings.example.co.uk</div>

<header class="abs header">
  <div class="abs brand">
    <div class="brand-mark"></div>
    <div>
      <div class="brand-name">Thornbury</div>
      <div class="brand-sub">Lettings Managment Ltd</div>
    </div>
  </div>
  <nav>
    <span class="abs nav active" style="left:666px">HOME</span>
    <span class="abs nav" style="left:772px">ABOUT</span>
    <span class="abs nav" style="left:883px">SERVICES</span>
    <span class="abs nav" style="left:1016px">CONTACT</span>
  </nav>
</header>

<section class="abs hero" role="img" aria-label="Close-up of a road map of Bristol with a blue push pin marking the city"></section>
<div class="abs hero-label hero-welcome">WELCOME</div>
<div class="abs hero-label hero-line" style="top:471px">To Thornbury Lettings Managment</div>
<div class="abs hero-label hero-line" style="top:512px">High Quality Real Estate in Bristol</div>

<div class="abs to-top" style="top:594px"><svg width="12" height="8" viewBox="0 0 12 8"><path d="M1 7 6 2l5 5" fill="none" stroke="#fff" stroke-width="2"/></svg></div>

<!-- services -->
<div class="abs service-photo" style="left:109px;background:linear-gradient(180deg,#3f7fd6 0%,#8fb4e3 45%,#e8ecee 70%,#c9cdd0 100%)" role="img" aria-label="Modern apartment block with balconies under a blue sky"></div>
<div class="abs service-photo" style="left:449px;background:linear-gradient(180deg,#4a86d8 0%,#9cbde4 45%,#9aa3a8 70%,#4a5a62 100%)" role="img" aria-label="Harbourside office buildings and cranes beside the water"></div>
<div class="abs service-photo" style="left:791px;background:linear-gradient(180deg,#7aa6de 0%,#cfdbe9 35%,#e9e6df 60%,#6f7070 100%)" role="img" aria-label="Curved Georgian terrace of townhouses"></div>

<h3 class="abs service-title" style="left:109px">LANDLORDS</h3>
<h3 class="abs service-title" style="left:449px">AGENCIES</h3>
<h3 class="abs service-title" style="left:791px">TENANTS</h3>

<div class="abs service-copy" style="left:109px">Lid est laborum dolo rumes fugats untras. Etha rums ser quidem rerums facilis dolores nemis onis fugats vitaes nemo minima rerums unsers sadips amets. Ut enim ad minim veniam, quis nostrud neque porro quisquam Ut enim ad minim veniam, quis nostrud Neque porro quisquam est, qui dolorem ipsum quia dolor sit amet, consectetur, adipisci amets uns. Nemo enim ipsam voluptatem quia voluptas sit aspernatur aut odit aut fugit.<span class="service-link">Find Out More...</span></div>
<div class="abs service-copy" style="left:449px">Lid est laborum dolo rumes fugats untras. Etha rums ser quidem rerums facilis dolores nemis onis fugats vitaes nemo minima rerums unsers sadips amets. Ut enim ad minim veniam, quis nostrud neque porro quisquam Ut enim ad minim veniam, quis nostrud Neque porro quisquam est, qui dolorem ipsum quia dolor sit amet, consectetur, adipisci amets uns. Nemo enim ipsam voluptatem quia voluptas sit aspernatur aut odit aut fugit, sed quia consequuntur magni dolores eos qui ratione voluptatem sequi nesciunt. Asunt in anim uis aute irure dolor in reprehenderit in voluptate velit esse cillumsert.<span class="service-link">Find Out More...</span></div>
<div class="abs service-copy" style="left:791px">Lid est laborum dolo rumes fugats untras. Etha rums ser quidem rerums facilis dolores nemis onis fugats vitaes nemo minima rerums unsers sadips amets. Ut enim ad minim veniam, quis nostrud neque porro quisquam Ut enim ad minim veniam, quis nostrud Neque porro quisquam est.<span class="service-link">Find Out More...</span></div>

<div class="abs to-top" style="top:1001px"><svg width="12" height="8" viewBox="0 0 12 8"><path d="M1 7 6 2l5 5" fill="none" stroke="#fff" stroke-width="2"/></svg></div>

<!-- divider -->
<div class="abs divider-line" style="top:1367px"></div>
<div class="abs divider-diamond" style="left:582px;top:1350px"></div>
<div class="abs to-top" style="top:1411px"><svg width="12" height="8" viewBox="0 0 12 8"><path d="M1 7 6 2l5 5" fill="none" stroke="#fff" stroke-width="2"/></svg></div>

<!-- reliability -->
<h2 class="abs section-title" style="left:109px;top:1474px">We manage your estate<br>with proven reliablity</h2>

<div class="abs stat" style="top:1614px"><div class="stat-fill" style="width:63%">Any kind of statistic goes here 63</div></div>
<div class="abs stat" style="top:1659px"><div class="stat-fill striped" style="width:95%">Tenant Satisfaction 95</div></div>
<div class="abs stat" style="top:1704px"><div class="stat-fill" style="width:98%">Time Property has sitting tenant 98</div></div>
<div class="abs stat" style="top:1747px"><div class="stat-fill striped" style="width:29%"></div><span class="stat-label">Any kind of statistic goes here 35</span></div>

<div class="abs bridge-photo" role="img" aria-label="Suspension bridge over a wooded gorge with hot air balloons in the sky"></div>
<div class="abs to-top" style="top:1817px"><svg width="12" height="8" viewBox="0 0 12 8"><path d="M1 7 6 2l5 5" fill="none" stroke="#fff" stroke-width="2"/></svg></div>

<div class="abs divider-line" style="top:1961px"></div>
<div class="abs divider-diamond" style="left:582px;top:1944px"></div>

<!-- testimonials -->
<h2 class="abs section-title" style="left:109px;top:2043px">Our satisfied customers</h2>
<blockquote class="abs quote">Lid est laborum dolo rumes fugats untras. Etha rums ser quidem rerums facilis dolores nemis onis fugats vitaes nemo minima rerums unsers sadips amets. Ut enim ad minim veniam, quis nostrud neque porro quisquam Ut enim ad minim veniam, quis nostrud Neque porro quisquam est, qui dolorem ipsum quia dolor</blockquote>
<div class="abs quote-tail"></div>
<div class="abs author">
  <svg width="22" height="26" viewBox="0 0 22 26"><circle cx="11" cy="7" r="6" fill="#333"/><path d="M1 26c0-7 4-11 10-11s10 4 10 11z" fill="#333"/></svg>
  <span><b>Helen Marsh</b>, Landlord</span>
</div>
<div class="abs to-top" style="top:2224px"><svg width="12" height="8" viewBox="0 0 12 8"><path d="M1 7 6 2l5 5" fill="none" stroke="#fff" stroke-width="2"/></svg></div>

<div class="abs thin-rule"></div>

<!-- connections -->
<h2 class="abs section-title" style="left:109px;top:2320px">Our trusted local<br>connections</h2>
<div class="abs arrow-btn" style="left:517px"><svg width="8" height="12" viewBox="0 0 8 12"><path d="M7 1 2 6l5 5" fill="none" stroke="#fff" stroke-width="2"/></svg></div>
<div class="abs badge" style="left:569px;top:2341px;width:150px;height:41px" aria-label="safehold-example.co.uk membership badge"></div>
<div class="abs badge" style="left:778px;top:2329px;width:52px;height:67px" aria-label="KTB membership badge"></div>
<div class="abs badge" style="left:899px;top:2308px;width:135px;height:109px" aria-label="GMV membership badge"></div>
<div class="abs arrow-btn" style="left:1066px"><svg width="8" height="12" viewBox="0 0 8 12"><path d="M1 1l5 5-5 5" fill="none" stroke="#fff" stroke-width="2"/></svg></div>

<!-- footer -->
<div class="abs footer-band"></div>

<div class="abs footer-brand">
  <div class="brand-mark"></div>
  <div><div class="name">Thornbury</div><div class="sub">Lettings Managment Ltd</div></div>
</div>
<p class="abs footer-about">Thornbury Lettings Managment Ltd Lorem ipsum ex vix illud nonummy, novum tation et his. At vix scriptaset patrioque scribentur, at pro fugit erts verterem molestiae, sed et vivendo ali Lorem ipsum ex vix illud nonummy, novum tation et his. At vix scripta patrioque scribentur...</p>

<h4 class="abs footer-heading" style="left:362px">MENU</h4>
<ul class="abs footer-menu">
  <li class="current">HOME</li>
  <li style="padding-top:11px">ABOUT</li>
  <li style="padding-top:11px">SERVICES</li>
  <li style="padding-top:11px">CONTACT</li>
</ul>

<h4 class="abs footer-heading" style="left:614px">CONTACT DETAILS</h4>
<div class="abs contact">Phone: 0117 496 0238<br>Email: <span>hello@thornburylettings.example.co.uk</span><br>Web:<br><span>www.thornburylettings.example.co.uk</span></div>

<h4 class="abs footer-heading" style="left:866px">GET IN TOUCH</h4>
<div class="abs field-label" style="top:2600px">Your Name (required)</div>
<div class="abs field" style="top:2618px;height:30px"></div>
<div class="abs field-label" style="top:2652px">Your Email (required)</div>
<div class="abs field" style="top:2667px;height:32px"></div>
<div class="abs field-label" style="top:2702px">Organisation</div>
<div class="abs field" style="top:2717px;height:33px"></div>
<div class="abs field-label" style="top:2752px">Your Message</div>
<div class="abs field" style="top:2767px;height:139px"></div>
<div class="abs send">Send</div>

<div class="abs to-top" style="top:2632px"><svg width="12" height="8" viewBox="0 0 12 8"><path d="M1 7 6 2l5 5" fill="none" stroke="#fff" stroke-width="2"/></svg></div>

<footer class="abs bottombar">Copyright 2016 Thornbury Lettings Managment | All Rights Reserved</footer>
<span class="abs social" style="left:876px"></span>
<span class="abs social" style="left:906px"></span>
<span class="abs social" style="left:936px"></span>
<span class="abs social" style="left:966px"></span>
<span class="abs social" style="left:996px"></span>
<span class="abs social" style="left:1026px"></span>
<span class="abs social" style="left:1056px"></span>
<div class="abs to-top" style="top:3023px;background:#3a3a3a"><svg width="12" height="8" viewBox="0 0 12 8"><path d="M1 7 6 2l5 5" fill="none" stroke="#fff" stroke-width="2"/></svg></div>

</body>
</html>
```